Gorgeous A5 Booklet 8pp - Existing Branding

Please transform a PDF text doc into an A5 booklet according to my existing branding, I need it fast.
I need to go to print.
Must be modern, fun, clean and classy design.
I can send images, logos and the .indd for the existing pdf to help you.
Thanks for being awesome!

We are a design agency so it needs to be good...we are too busy to create it.

Front cover can have open paragraph.
Back cover must have contact details
three inside spreads should have the 11 essentials.

The executive summary attached is a good example of the look and feel you can copy.

Please let me know if you have any questions.
Thanks
Light ahead!
:)

Target Market(s)

entreprenuers and small business owners

Industry/Entity Type

Design Agency

Font styles to use
Sans Serif

Colors
e34197
fff5ee
333333
faa54b
acd036
33a6d7

Requirements
Must have
• font is century gothic - no bold
gudea body text
sketch rockwell
seans hand

see website www.tidelantern.com.au for branding
or match to pdf attached with origami images

Colours in palette below of only indicative. actual colours are as per website colour strip.
Should not have
• not too pink
not too many stars

```html
<!DOCTYPE html>
<html lang="en">
<head>
<meta charset="utf-8">
<title>11 Essentials for a Successful Website – Booklet Spread</title>
<link href="https://fonts.googleapis.com/css2?family=Gudea:wght@400&family=Questrial&family=Zilla+Slab:wght@500;600&display=swap" rel="stylesheet">
<style>
  :root {
    --pink: #e34197;
    --cream: #fff5ee;
    --ink: #333333;
    --body: #4a4a4a;
    --orange: #faa54b;
    --green: #acd036;
    --blue: #33a6d7;
    --teal: #5ab7b4;
    --stage: #e9e9ea;
    --paper: #ffffff;
  }
  * { box-sizing: border-box; margin: 0; padding: 0; }
  html, body { width: 1200px; height: 900px; overflow: hidden; }
  body {
    background: var(--stage);
    font-family: "Gudea", "Trebuchet MS", sans-serif;
    color: var(--body);
  }
  .spread {
    position: absolute;
    left: 36px; top: 48px;
    width: 1128px; height: 804px;
    display: flex;
    box-shadow: 0 10px 30px rgba(0,0,0,.12);
  }
  .page {
    position: relative;
    width: 564px; height: 804px;
    background: var(--paper);
    overflow: hidden;
  }
  .page--left { background: linear-gradient(to left, #ececec 0, #fff 28px); }
  .page--right { background: linear-gradient(to right, #e6e6e6 0, #fff 28px); }

  .hero {
    position: absolute;
    top: 22px; height: 312px;
  }
  .page--left .hero { left: 20px; right: 28px; }
  .page--right .hero { left: 28px; right: 20px; }
  .hero__photo {
    position: absolute; inset: 0 0 0 16px;
  }
  .page--right .hero__photo { inset: 0 16px 0 16px; }
  .hero__photo--office { background: linear-gradient(135deg, #cfd6dc 0%, #eef0f1 45%, #b9bec2 100%); }
  .hero__photo--team { background: linear-gradient(135deg, #d8d2c8 0%, #9fb7bf 45%, #c98c86 100%); }

  .colour-strip {
    position: absolute; top: 0; bottom: 0; width: 16px;
    display: flex; flex-direction: column;
  }
  .colour-strip--start { left: 0; }
  .colour-strip--end { right: 0; }
  .colour-strip span { flex: 1; }
  .colour-strip .s-teal { background: var(--teal); }
  .colour-strip .s-pink { background: var(--pink); }
  .colour-strip .s-green { background: var(--green); }
  .colour-strip .s-orange { background: var(--orange); }
  .colour-strip .s-grey { background: #d9d4cf; flex: 2; }

  .hero__title {
    position: absolute; left: 16px; right: 0; bottom: 34px;
    padding: 6px 24px 8px;
    background: rgba(255,255,255,.45);
    font-family: "Zilla Slab", "Rockwell", serif;
    color: #fff;
    text-shadow: 1px 1px 0 #7d7d7d, -1px -1px 0 #9a9a9a;
    text-align: right;
  }
  .page--right .hero__title { right: 16px; }
  .hero__title small { display: block; font-size: 22px; font-weight: 500; line-height: 1.1; padding-right: 140px; }
  .hero__title strong { display: block; font-size: 36px; font-weight: 600; line-height: 1.05; }

  .copy {
    position: absolute;
    top: 350px;
    font-size: 12.4px;
    line-height: 1.38;
  }
  .page--left .copy { left: 34px; right: 44px; }
  .page--right .copy { left: 52px; right: 30px; }
  .copy p { margin-bottom: 9px; }
  .copy .indent { padding-left: 16px; }
  .essential__head { color: var(--pink); }

  .illustration {
    position: absolute;
    border-radius: 4px;
  }
  .illustration--butterfly {
    right: 64px; bottom: 22px; width: 44px; height: 44px;
    background: linear-gradient(135deg, #ffd060, var(--orange));
  }
  .illustration--elephant {
    left: 52px; bottom: 56px; width: 92px; height: 52px;
    background: linear-gradient(135deg, #a6d85a, #5ea336);
  }

  .brand {
    position: absolute; bottom: 22px;
    display: flex; align-items: center; gap: 7px;
    font-family: "Questrial", "Century Gothic", sans-serif;
    font-size: 27px; color: var(--pink); letter-spacing: .5px;
  }
  .page--left .brand { left: 30px; }
  .page--right .brand { right: 34px; }
  .brand__dot { width: 9px; height: 9px; border-radius: 50%; background: var(--pink); }

  .edge-band {
    position: absolute; left: 0; right: 0; bottom: 0; height: 6px;
    background: linear-gradient(to right, var(--blue) 0 25%, var(--pink) 25% 50%, var(--green) 50% 75%, var(--orange) 75% 100%);
  }
</style>
</head>
<body>
  <main class="spread">
    <section class="page page--left">
      <div class="hero">
        <div class="colour-strip colour-strip--start">
          <span class="s-grey"></span><span class="s-teal"></span><span class="s-pink"></span><span class="s-green"></span><span class="s-orange"></span>
        </div>
        <div class="hero__photo hero__photo--office" role="img" aria-label="Photograph of a smiling businesswoman in a bright modern office"></div>
        <h2 class="hero__title"><small>11 Essentials for a</small><strong>Successful website</strong></h2>
      </div>

      <div class="copy">
        <p><span class="essential__head">1. Perfect Elevator Pitch:</span> Studies show that website visitors spend an average of seven seconds or less on 90% of the websites they visit. This means you only have a few short moments to convey who you are, what you do, who you do it for, and why you're the best choice. Make sure you nail your pitch and get it front and center on your homepage.</p>
        <p class="indent">It's important to spend time honing your core marketing message and ensuring that your logo, tagline and the initial two sentences of your website copy are clear and present your brand with credibility and impact, succinctly outlining your specialty and target market. It's a lot to communicate in very little time so your pitch must be concise and compelling.</p>
        <p><span class="essential__head">2. Clear Call to Actions:</span> When small business owners ask, "Why isn't my website converting?" the answer is most often a lack of call to actions. Common call to actions include phone numbers and 'Buy Now' buttons, but they may also be more subtle actions encouraging visitors to a next step. Call to actions are designed to engage your visitors and guide them down the path to a conversion. Visitors to your website need specific information before committing to a purchase or enquiry; smart call to actions preempt the visitor's next step and gently lead them through your website in the way you want them to experience your website while delivering the information they are seeking.</p>
        <p class="indent">On the most basic level make sure your phone number is in the top right of every page of your site. Put your contact info on the footer of every page along with quick links to your most valuable content. This is even more important for mobile websites where prospects are often just looking for a quick phone number, hours or address.</p>
      </div>

      <div class="illustration illustration--butterfly" role="img" aria-label="Orange origami butterfly illustration"></div>
      <div class="brand"><span class="brand__name">tidelantern</span><span class="brand__dot"></span></div>
      <div class="edge-band"></div>
    </section>

    <section class="page page--right">
      <div class="hero">
        <div class="colour-strip colour-strip--start">
          <span class="s-teal"></span><span class="s-pink"></span><span class="s-grey"></span><span class="s-green"></span><span class="s-orange"></span>
        </div>
        <div class="hero__photo hero__photo--team" role="img" aria-label="Photograph of two men reviewing documents together at a desk"></div>
        <div class="colour-strip colour-strip--end">
          <span class="s-teal"></span><span class="s-pink"></span><span class="s-grey"></span><span class="s-green"></span><span class="s-orange"></span>
        </div>
        <h2 class="hero__title"><small>11 Essentials for a</small><strong>Successful website</strong></h2>
      </div>

      <div class="copy">
        <p><span class="essential__head">3. Track your Conversations:</span> We mention conversion tracking up the top because it's so often neglected, yet it's one of the easiest strategies to implement. It is vital to know how many enquiries and sales that you receive through your website, where those website visitors come from and what the cost is to acquire them. This allows you to accurately measure your marketing spend, evaluate the success of any improvements or modifications in your website design or online marketing, and ultimately measure the underlying success of your website.</p>
        <p><span class="essential__head">4. Engaging "About Us" Page:</span> The two biggest mistakes made with About Us pages is that they are often boring, and they're not about the customer. It may seem counter-intuitive to write an About Us page that is more about your customer than your company, but there's a good reason for it.</p>
        <p>Your company exists for your customer. So by logical extension, your About Us page is also about your customer. That's not to say it shouldn't create an engaging portrait of the personalities behind your organisation because your prospects want to know who they're working with, but they also want to know how those people are going to make their lives better. Your About Us page, like the rest of your website, should present all information in the context of how it benefits your visitors.</p>
      </div>

      <div class="illustration illustration--elephant" role="img" aria-label="Green origami elephant illustration"></div>
      <div class="brand"><span class="brand__name">tidelantern</span><span class="brand__dot"></span></div>
      <div class="edge-band"></div>
    </section>
  </main>
</body>
</html>
```